Fitness Equipment Repair Business Needs a Catchy New Business Card

We have an existing business card, however, it is quite plain and boring. We are expanding primarily in the commercial area (gyms, studios, apartment complexes etc). The business card will serve as eye candy to those managers/owners that can't be met for a face to face.
Originally I was planning for a brochure as well, but all of our information is better summarized on our website. (brasswheelservicing.ca).
I would like the card to match the colour scheme of the website and utilize the logo. It should have a professional clean feel to it, however, a little colouring outside the lines wouldn't hurt.
The example card is for my service technician (Corwin Haldane). If possible I would like to be able to edit the text to use for more than one person.

Industry/Entity Type

Appliance Repair

Contact Information for Business Card

Clean, crisp and professional but needs to be eye catching. Preferably using the black, white and red colour scheme matching the website. Double sided would be nice, but is not necessary.

Colors
ec1f27
ffffff
000000

Requirements
Must have
• Must be able to edit name, phone number and title to use for multiple people. Must show the company website (brasswheelservicing.ca).

```html
<!DOCTYPE html>
<html lang="en">
<head>
<meta charset="utf-8">
<title>Brass Wheel Servicing – Business Card</title>
<link href="https://fonts.googleapis.com/css2?family=Didact+Gothic&family=Raleway:ital,wght@0,500;0,700;1,500&display=swap" rel="stylesheet">
<style>
  :root {
    --red: #ec1f27;
    --white: #ffffff;
    --black: #000000;
    --backdrop: #dcd8d2;
    --text-font: "Didact Gothic", sans-serif;
    --head-font: "Raleway", sans-serif;
  }
  * { margin: 0; padding: 0; box-sizing: border-box; }
  html, body {
    width: 1200px; height: 987px; overflow: hidden;
    background: var(--backdrop);
  }
  .card {
    position: absolute; left: 293px; width: 615px; height: 345px;
    box-shadow: 0 6px 18px rgba(0,0,0,.35);
    overflow: hidden;
  }
  .card-front { top: 131px; background: var(--black); color: var(--white); font-family: var(--text-font); }
  .card-back { top: 506px; height: 350px; background: var(--red); color: var(--white); }

  .brand-mark {
    position: absolute; left: 262px; top: 36px;
    width: 84px; height: 84px; border: 2px solid var(--white); border-radius: 50%;
  }
  .brand-name {
    position: absolute; left: 378px; top: 76px;
    font-family: var(--head-font); font-weight: 700; font-size: 15px;
    font-variant: small-caps; letter-spacing: 1px; color: var(--white);
  }
  .person-name {
    position: absolute; left: 33px; top: 176px;
    font-family: var(--head-font); font-weight: 700; font-size: 22px;
    font-variant: small-caps; letter-spacing: 1.5px; color: var(--red);
  }
  .person-title {
    position: absolute; left: 33px; top: 204px;
    font-family: var(--head-font); font-weight: 500; font-size: 16px;
    font-variant: small-caps; letter-spacing: 1px; color: var(--white);
  }
  .divider {
    position: absolute; left: 33px; top: 236px; width: 551px; height: 1px; background: var(--white);
  }
  .contact-list { position: absolute; left: 33px; top: 250px; list-style: none; font-size: 15px; }
  .contact-list li { display: flex; align-items: center; height: 23.5px; }
  .contact-list svg { width: 14px; height: 14px; margin-right: 10px; fill: var(--red); }
  .address {
    position: absolute; right: 31px; top: 250px; text-align: right; font-size: 15px; line-height: 23.5px;
  }
  .address .website { color: var(--red); }
  .edge-white { position: absolute; left: 0; bottom: 7px; width: 100%; height: 4px; background: var(--white); }
  .edge-red { position: absolute; left: 0; bottom: 0; width: 100%; height: 7px; background: var(--red); }

  .back-mark {
    position: absolute; left: 252px; top: 62px;
    width: 110px; height: 110px; border: 2px solid var(--white); border-radius: 50%;
  }
  .back-name {
    position: absolute; left: 0; width: 100%; top: 198px; text-align: center;
    font-family: var(--head-font); font-weight: 700; font-size: 26px;
    font-variant: small-caps; letter-spacing: 1.5px; color: var(--white);
  }
  .back-website {
    position: absolute; left: 0; width: 100%; top: 282px; text-align: center;
    font-family: var(--head-font); font-style: italic; font-weight: 500; font-size: 17px;
    letter-spacing: 1.2px; color: var(--white);
  }
</style>
</head>
<body>
  <section class="card card-front">
    <div class="brand-mark"></div>
    <div class="brand-name">Brass Wheel Servicing</div>

    <div class="person-name">Corwin Haldane</div>
    <div class="person-title">Service technician</div>
    <div class="divider"></div>

    <ul class="contact-list">
      <li><svg viewBox="0 0 24 24"><path d="M6.6 10.8a15.1 15.1 0 0 0 6.6 6.6l2.2-2.2a1 1 0 0 1 1-.25 11.4 11.4 0 0 0 3.6.57 1 1 0 0 1 1 1V20a1 1 0 0 1-1 1A17 17 0 0 1 3 4a1 1 0 0 1 1-1h3.5a1 1 0 0 1 1 1c0 1.25.2 2.45.57 3.57a1 1 0 0 1-.25 1z"/></svg>587-555-0148</li>
      <li><svg viewBox="0 0 24 24"><path d="M6.6 10.8a15.1 15.1 0 0 0 6.6 6.6l2.2-2.2a1 1 0 0 1 1-.25 11.4 11.4 0 0 0 3.6.57 1 1 0 0 1 1 1V20a1 1 0 0 1-1 1A17 17 0 0 1 3 4a1 1 0 0 1 1-1h3.5a1 1 0 0 1 1 1c0 1.25.2 2.45.57 3.57a1 1 0 0 1-.25 1z"/></svg>780-555-0193</li>
      <li><svg viewBox="0 0 24 24"><path d="M2 5h20v14H2z M2 5l10 8 10-8" /></svg>service@brasswheel.ca</li>
    </ul>

    <div class="address">
      1875 Larchmont Way NW<br>
      Edmonton AB T5X 0K2<br>
      <span class="website">www.brasswheelservicing.ca</span>
    </div>

    <div class="edge-white"></div>
    <div class="edge-red"></div>
  </section>

  <section class="card card-back">
    <div class="back-mark"></div>
    <div class="back-name">Brass Wheel Servicing</div>
    <div class="back-website">www.brasswheelservicing.ca</div>
  </section>
</body>
</html>
```